Smartphone App
Zielgruppe
Wir vertreiben ein Produkt (Name: Vorlix) mit dem Smartphone Apps erstellt werden können, quasi ein CMS für Smartphone Apps. Wir verkaufen dem Kunden das Produkt und dazu die Dienstleistung das Produkt beim Kunden zu installieren und zu personalisieren Analog zur Einrichtung eines CMS für eine Webseite.
Aufgabenstellung
Wir benötigen einen Flyer A4 den wir per Briefpost zur Kaltaquise versenden können.
Die Message die wir transportieren möchten ist, dass man heute mit einer Smartphone App neue Möglichkeiten hat, Informationen zum Kunden (Stammkunden) zu kommunizieren. Dass es einfach und schnell geht, eine eigene App zu haben und dass die Pflege kinderleicht ist und keine Fachkenntnisse erfordert. Schlagworte bezügl. der Funktionen der App: Informationen, Push-Nachrichten, Terminkalender, Reservierung, Verkauf, Bestellung. Der Leser soll neugierig darauf werden und einen Termin für eine unverbindliche Beratung vereinbaren. Bilder sollten Smartphone und Kundenbindung rüberbringen. Das Design sollte die Zielgruppe Gastronomen und Einzelhändler, also in der Regel Inhaber geführte Geschäfte ansprechen. Auf den Flyer sollten Informationen zu uns sein.

```html
<!DOCTYPE html>
<html lang="de">
<head>
<meta charset="utf-8">
<title>Vorlix – Flyer Vorder- und Rückseite</title>
<link rel="stylesheet" href="https://fonts.googleapis.com/css2?family=Cabin:wght@400;500;600&family=Cabin+Condensed:wght@500;600;700&display=swap">
<style>
  :root {
    --green: #6ab06a;
    --green-dark: #4e8a55;
    --green-deep: #3f7447;
    --white: #ffffff;
    --photo-top: #b9c7cf;
    --photo-mid: #8a7a6e;
    --photo-low: #5b4a40;
    --round-photo: #c9dbe6;
    --text-dark: #333333;
  }
  * { margin: 0; padding: 0; box-sizing: border-box; }
  html, body { width: 1200px; height: 1200px; overflow: hidden; background: var(--white); }
  .canvas { position: relative; width: 1200px; height: 1200px; background: var(--white); }

  .flyer {
    position: absolute; top: 258px; width: 436px; height: 615px;
    background: var(--green); overflow: hidden;
    box-shadow: 6px 8px 10px rgba(0,0,0,0.28);
    font-family: "Cabin Condensed", "Arial Narrow", sans-serif;
    color: var(--white);
  }
  .flyer--front { left: 73px; }
  .flyer--back { left: 663px; }
  .flyer__bg { position: absolute; inset: 0; width: 436px; height: 615px; }

  /* front */
  .front-title {
    position: absolute; left: 30px; top: 382px;
    font-family: "Cabin", sans-serif; font-weight: 500;
    font-size: 52px; line-height: 1; letter-spacing: -0.5px;
  }
  .front-sub {
    position: absolute; left: 30px; top: 447px;
    font-family: "Cabin", sans-serif; font-weight: 500;
    font-size: 21px; line-height: 35px;
  }
  .front-brand {
    position: absolute; right: 10px; top: 518px;
    font-family: "Cabin", sans-serif; font-weight: 600; font-size: 18px;
  }
  .social-strip {
    position: absolute; left: 0; top: 574px; width: 436px; height: 29px;
    display: flex; justify-content: center; align-items: center; gap: 8px;
    color: var(--text-dark); font-family: "Cabin", sans-serif; font-size: 11px;
    letter-spacing: 0.5px;
  }
  .social-item { display: flex; align-items: center; gap: 3px; }
  .social-item__mark { width: 11px; height: 11px; background: var(--green-dark); }

  /* back */
  .back-headline {
    position: absolute; left: 26px; top: 44px;
    font-family: "Cabin", sans-serif; font-weight: 500;
    font-size: 30px; line-height: 28px; color: var(--green);
  }
  .back-copy {
    position: absolute; font-weight: 600; font-size: 12.5px; line-height: 17px;
  }
  .back-copy--one { left: 15px; top: 152px; width: 150px; }
  .back-copy--two { left: 277px; top: 235px; width: 150px; }
  .back-copy--three { left: 17px; top: 298px; width: 140px; }
  .back-copy--four { left: 227px; top: 345px; width: 140px; }
  .back-cta {
    position: absolute; left: 26px; top: 460px; width: 340px;
    font-weight: 600; font-size: 22px; line-height: 30px;
  }
  .contact-strip {
    position: absolute; left: 0; top: 573px; width: 436px; height: 30px;
    display: flex; align-items: center; justify-content: space-between;
    padding: 0 8px; color: var(--green);
    font-weight: 700; font-size: 13px; white-space: nowrap;
  }
  .contact-item { display: flex; align-items: center; gap: 3px; }
  .contact-item svg { width: 17px; height: 17px; }
</style>
</head>
<body>
<div class="canvas">

  <!-- Vorderseite -->
  <section class="flyer flyer--front">
    <svg class="flyer__bg" viewBox="0 0 436 615" aria-hidden="true">
      <defs>
        <linearGradient id="photoTone" x1="0" y1="0" x2="0" y2="1">
          <stop offset="0" stop-color="var(--photo-top)"/>
          <stop offset="0.55" stop-color="var(--photo-mid)"/>
          <stop offset="1" stop-color="var(--photo-low)"/>
        </linearGradient>
        <linearGradient id="roundTone" x1="0" y1="0" x2="1" y2="1">
          <stop offset="0" stop-color="#eef4f8"/>
          <stop offset="1" stop-color="var(--round-photo)"/>
        </linearGradient>
      </defs>
      <rect class="hero-photo" x="0" y="0" width="436" height="345" fill="url(#photoTone)" role="img" aria-label="Foto: Gruppe junger Menschen am Tisch mit Smartphones und Tablets"/>
      <path d="M0 190 C 90 280, 240 335, 436 335 L436 615 L0 615 Z" fill="var(--green-dark)"/>
      <path d="M0 232 C 110 320, 260 355, 436 350 L436 615 L0 615 Z" fill="var(--green)"/>
      <circle cx="109" cy="304" r="58" fill="var(--green-dark)"/>
      <circle cx="109" cy="304" r="49" fill="url(#roundTone)" role="img" aria-label="Foto: Händedruck zweier Geschäftspartner"/>
      <path d="M0 565 C 120 535, 300 530, 436 560 L436 615 L0 615 Z" fill="var(--green-dark)"/>
      <rect x="0" y="574" width="436" height="29" fill="var(--white)"/>
      <rect x="0" y="603" width="436" height="12" fill="var(--green-dark)"/>
    </svg>

    <h1 class="front-title">Ihre eigene App,</h1>
    <p class="front-sub">kinderleicht &amp; ohne Fachkentnisse.<br>sofort verfügbar &amp; einfachste Bedienung.</p>
    <p class="front-brand">mit Vorlix®</p>

    <div class="social-strip">
      <span class="social-item"><span class="social-item__mark"></span>/VORLIX</span>
      <span class="social-item"><span class="social-item__mark"></span>@VORLIX</span>
      <span class="social-item"><span class="social-item__mark"></span>/VORLIX</span>
    </div>
  </section>

  <!-- Rückseite -->
  <section class="flyer flyer--back">
    <svg class="flyer__bg" viewBox="0 0 436 615" aria-hidden="true">
      <defs>
        <linearGradient id="screenTone" x1="0" y1="0" x2="1" y2="1">
          <stop offset="0" stop-color="#2a2a2a"/>
          <stop offset="0.6" stop-color="#4a5a3a"/>
          <stop offset="1" stop-color="#1c1c1c"/>
        </linearGradient>
      </defs>
      <polygon points="0,30 436,20 436,106 0,142" fill="var(--white)"/>
      <circle cx="274" cy="164" r="55" fill="var(--text-dark)"/>
      <circle cx="274" cy="164" r="51" fill="var(--white)"/>
      <circle cx="274" cy="164" r="46" fill="url(#screenTone)" role="img" aria-label="Foto: Smartphone und Smartwatch mit geöffneter App"/>
      <circle cx="206" cy="248" r="55" fill="var(--text-dark)"/>
      <circle cx="206" cy="248" r="51" fill="var(--white)"/>
      <circle cx="206" cy="248" r="46" fill="url(#screenTone)" role="img" aria-label="Foto: Tablet, Smartphone und Laptop mit der App"/>
      <path d="M0 562 C 130 530, 300 528, 436 556 L436 615 L0 615 Z" fill="var(--green-dark)"/>
      <rect x="0" y="573" width="436" height="30" fill="var(--white)"/>
      <rect x="0" y="603" width="436" height="12" fill="var(--green)"/>
    </svg>

    <h2 class="back-headline">Optimieren Sie ihr Geschäft<br>und bieten Sie ihren Kunden<br>etwas.</h2>

    <p class="back-copy back-copy--one">Durch ihre eigene App, können Sie mit ihren Kunden besser kommunizieren und ihr Geschäft vermarkten.</p>
    <p class="back-copy back-copy--two">Die App beinhaltet beispielsweise Push-Nachrichten mit der Sie ihre Informationen direkt an die Kunden vermitteln können.</p>
    <p class="back-copy back-copy--three">Aber auch Reservierungen oder Bestellungen sind mit der App sofort realisierbar.</p>
    <p class="back-copy back-copy--four">Zudem gibt es noch weitere Features der App, die je nach Unternehmen verwendet werden können.</p>

    <p class="back-cta">Falls ihre Interesse geweckt wurde, vereinbaren Sie doch einfach einen Termin für eine professionelle Beratung !</p>

    <div class="contact-strip">
      <span class="contact-item">ITservice-Partner</span>
      <span class="contact-item">
        <svg viewBox="0 0 20 20" aria-hidden="true"><circle cx="10" cy="10" r="9.5" fill="var(--green-dark)"/><circle cx="10" cy="7.5" r="3.2" fill="var(--white)"/><path d="M4.5 16 C5.5 12, 14.5 12, 15.5 16 Z" fill="var(--white)"/></svg>
        JONAS BERGLIND
      </span>
      <span class="contact-item">
        <svg viewBox="0 0 20 20" aria-hidden="true"><path d="M10 1 C5.5 1 3 4.2 3 7.5 C3 12 10 19 10 19 C10 19 17 12 17 7.5 C17 4.2 14.5 1 10 1 Z" fill="var(--green-dark)"/><circle cx="10" cy="7.5" r="2.6" fill="var(--white)"/></svg>
        KELSDORF
      </span>
      <span class="contact-item">
        <svg viewBox="0 0 20 20" aria-hidden="true"><rect x="0.5" y="0.5" width="19" height="19" rx="3" fill="var(--green-dark)"/><path d="M6 4 L8.3 4 L9.2 7.3 L7.8 8.6 C8.6 10.3 9.7 11.4 11.4 12.2 L12.7 10.8 L16 11.7 L16 14 C16 15 15.2 15.8 14.2 15.6 C9 14.7 5.3 11 4.4 5.8 C4.2 4.8 5 4 6 4 Z" fill="var(--white)"/></svg>
        TEL.: 02100-554318
      </span>
    </div>
  </section>

</div>
</body>
</html>
```